Leaf Haven Business Card Design

My E-Commerce store is called Leaf Haven

Website address is - http://www.leafhaven-demo.com.au

I would like a colourful, friendly business with the description in the 'must haves' box incorporated into it
Updates

Please add the following to the business cards; Natural & Organic Products Online Organic Pantry Items Superfoods & Supplements Natural Skincare Eco Friendly Household Products

Industry/Entity Type

Business

Contact Information for Business Card

www.leafhaven-demo.com.au
mira@leafhaven-demo.com.au

Colors
acd037
9bcb3c
cadf82
eaf2ce

Requirements
Must have
• Natural & Organic Eco Products Online.
• Leaf Haven specialises in organic pantry items, superfoods and supplements, organic skincare for you and your family & eco friendly household products.

```html
<!DOCTYPE html>
<html lang="en">
<head>
<meta charset="utf-8">
<title>Leaf Haven Business Card</title>
<link rel="stylesheet" href="https://fonts.googleapis.com/css2?family=Questrial&family=Open+Sans:wght@700&display=swap">
<style>
  :root {
    --backdrop: #3b3b3b;
    --card: #ffffff;
    --brand-green: #0ea04b;
    --name-green: #139c48;
    --role-grey: #a3a3a3;
    --contact-grey: #555555;
    --leaf-lime: #acd037;
    --leaf-green: #9bcb3c;
    --leaf-soft: #cadf82;
    --leaf-mist: #eaf2ce;
  }
  * { margin: 0; padding: 0; box-sizing: border-box; }
  html, body {
    width: 1105px;
    height: 1200px;
    overflow: hidden;
    background: var(--backdrop);
  }
  .canvas {
    position: relative;
    width: 1105px;
    height: 1200px;
  }
  .card {
    position: absolute;
    left: 196px;
    width: 720px;
    height: 411px;
    background: var(--card);
    border-radius: 22px;
    overflow: hidden;
    font-family: "Questrial", "Century Gothic", sans-serif;
    text-align: center;
  }
  .card--front { top: 146px; }
  .card--back  { top: 602px; }

  .card-band {
    position: absolute;
    left: 0;
    right: 0;
    bottom: 0;
    height: 10px;
    background: linear-gradient(90deg, var(--leaf-mist), var(--leaf-soft), var(--leaf-green), var(--leaf-lime));
  }

  .brand-name {
    color: var(--brand-green);
    font-family: "Questrial", "Century Gothic", sans-serif;
    font-weight: 400;
    line-height: 1;
    letter-spacing: -1px;
  }
  .card--front .brand-name {
    position: absolute;
    top: 62px;
    left: 0;
    right: 0;
    font-size: 76px;
  }
  .tagline {
    position: absolute;
    top: 160px;
    left: 0;
    right: 0;
    font-size: 19px;
    color: var(--leaf-green);
    letter-spacing: 0.5px;
  }

  .holder-name {
    position: absolute;
    top: 222px;
    left: 0;
    right: 0;
    font-family: "Open Sans", "Helvetica Neue", sans-serif;
    font-weight: 700;
    font-size: 25px;
    color: var(--name-green);
  }
  .holder-role {
    position: absolute;
    top: 260px;
    left: 0;
    right: 0;
    font-size: 20px;
    color: var(--role-grey);
  }
  .contact {
    position: absolute;
    top: 298px;
    left: 0;
    right: 0;
    font-size: 21px;
    line-height: 31px;
    color: var(--contact-grey);
    list-style: none;
  }

  .brand-lockup {
    position: absolute;
    top: 118px;
    left: 0;
    right: 0;
    display: flex;
    justify-content: center;
    align-items: center;
    gap: 18px;
  }
  .brand-dot {
    width: 30px;
    height: 30px;
    border-radius: 50%;
    background: var(--leaf-lime);
  }
  .card--back .brand-name { font-size: 62px; }

  .product-list {
    position: absolute;
    top: 232px;
    left: 60px;
    right: 60px;
    list-style: none;
    display: flex;
    flex-wrap: wrap;
    justify-content: center;
    gap: 10px 12px;
    font-size: 17px;
    color: var(--contact-grey);
  }
  .product-list li {
    padding: 6px 14px;
    border-radius: 16px;
    background: var(--leaf-mist);
  }
</style>
</head>
<body>
  <main class="canvas">
    <section class="card card--front" aria-label="Business card front">
      <h1 class="brand-name">Leaf Haven</h1>
      <p class="tagline">Natural &amp; Organic Eco Products Online</p>
      <p class="holder-name">Jordan Hale</p>
      <p class="holder-role">CEO/Founder</p>
      <ul class="contact">
        <li>mira@leafhaven-demo.com.au</li>
        <li>www.leafhaven-demo.com.au</li>
      </ul>
      <div class="card-band"></div>
    </section>

    <section class="card card--back" aria-label="Business card back">
      <div class="brand-lockup">
        <span class="brand-dot"></span>
        <p class="brand-name">Leaf Haven</p>
      </div>
      <ul class="product-list">
        <li>Organic Pantry Items</li>
        <li>Superfoods &amp; Supplements</li>
        <li>Natural Skincare</li>
        <li>Eco Friendly Household Products</li>
      </ul>
      <div class="card-band"></div>
    </section>
  </main>
</body>
</html>
```